Saffron Ledger Works Flyer

We need a one page promotional piece that explains what our company does, and the benefits it provides in a simple, elegant, easy to understand way. I would like to print it on glossy heavyweight paper to give a feel of high quality and legitimacy. I will include the logo, the tag line, and the main benefits that the company offers.

Tag line concept, may not need these exact words. "Give us 5 minutes a day, and we will help you build a Saffron Ledger Works."

Key points...(exact wording not required if you think of a better way to say it)

Software easy enough for my grandpa to use.
Lets you use snail mail, email, texting, and social media to quickly market to your customers at very low cost.
Web based which allows you to launch media campaigns from your desktop, or smartphone in moments.
Quick 3 - 5 minute training videos which give you hard hitting, quick action tips that will help you make your business better today.
Live coaching calls to help motivate you to improve your business.
No contracts, or start up fees. One low price of $299 per month.

Restaurant owners

Restaurant

```html
<!DOCTYPE html>
<html lang="en">
<head>
<meta charset="utf-8">
<title>Saffron Ledger Works Flyer</title>
<link rel="stylesheet" href="https://fonts.googleapis.com/css2?family=Archivo+Black&family=Source+Sans+3:wght@400;700&display=swap">
<style>
  :root {
    --page-bg: #e9e9e9;
    --sheet-white: #ffffff;
    --sheet-edge: #6c6c6c;
    --sky-light: #d7e6f7;
    --sky-mid: #aac7ea;
    --sky-deep: #9dbde6;
    --row-white: #ffffff;
    --link-blue: #1f5ca8;
    --ink-dark: #333333;
    --brand-grey: #5b5b5b;
    --headline-blue: #a6c6ec;
    --night: #0c0c0c;
    --night-haze: #3a3d40;
    --bill-green: #b9bfa7;
    --bill-shadow: #4f5547;
  }
  * { box-sizing: border-box; margin: 0; padding: 0; }
  html, body { width: 1200px; height: 848px; overflow: hidden; }
  body {
    background: var(--page-bg);
    font-family: "Source Sans 3", sans-serif;
    position: relative;
  }
  .flyer {
    position: absolute;
    left: 330px;
    top: 24px;
    width: 540px;
    height: 800px;
    background: var(--sheet-white);
    padding: 5px;
    box-shadow: 0 3px 8px rgba(0,0,0,0.35);
  }
  .flyer-inner {
    position: relative;
    width: 100%;
    height: 100%;
    border: 1px solid var(--sheet-edge);
    overflow: hidden;
  }
  .benefits-panel {
    position: absolute;
    left: 0; top: 0;
    width: 100%;
    height: 331px;
    background: radial-gradient(ellipse at 40% 35%, var(--sky-light) 0%, var(--sky-mid) 55%, var(--sky-deep) 100%);
  }
  .brand {
    position: absolute;
    left: 24px;
    top: 80px;
    width: 200px;
    text-align: center;
  }
  .brand-dot {
    display: block;
    width: 62px;
    height: 62px;
    margin: 0 auto 18px;
    border-radius: 50%;
    background: var(--brand-grey);
  }
  .brand-name {
    font-family: "Source Sans 3", sans-serif;
    font-weight: 700;
    font-size: 34px;
    line-height: 1.0;
    letter-spacing: 1px;
    text-transform: uppercase;
    color: var(--brand-grey);
  }
  .benefit-list {
    position: absolute;
    left: 250px;
    top: 30px;
    width: 283px;
    list-style: none;
  }
  .benefit {
    font-size: 13px;
    line-height: 1.2;
    padding: 4px 6px 5px;
    color: var(--ink-dark);
  }
  .benefit + .benefit { margin-top: 5px; }
  .benefit--highlight {
    background: var(--row-white);
    color: var(--link-blue);
  }
  .headline-band {
    position: absolute;
    left: 0; top: 331px;
    width: 100%;
    height: 200px;
    background: radial-gradient(ellipse at 50% 120%, var(--night-haze) 0%, var(--night) 70%);
    padding: 22px 0 0 20px;
  }
  .headline {
    font-family: "Archivo Black", sans-serif;
    color: var(--headline-blue);
    text-transform: uppercase;
    line-height: 0.9;
    white-space: nowrap;
    letter-spacing: -0.5px;
  }
  .headline span { display: block; }
  .headline .line-lead { font-size: 30px; }
  .headline .line-bridge { font-size: 24px; }
  .headline .line-name { font-size: 56px; }
  .headline .line-name-end { font-size: 52px; }
  .cash-image {
    position: absolute;
    left: 0; top: 531px;
    width: 100%;
    height: 269px;
    background:
      radial-gradient(ellipse at 50% 75%, var(--bill-green) 0%, #8f957d 45%, var(--bill-shadow) 75%, #2a2c2a 100%);
  }
</style>
</head>
<body>
  <main class="flyer">
    <div class="flyer-inner">
      <section class="benefits-panel">
        <div class="brand">
          <span class="brand-dot"></span>
          <p class="brand-name">Saffron<br>Ledger<br>Works</p>
        </div>
        <ul class="benefit-list">
          <li class="benefit benefit--highlight">Software easy enough for my grandpa to use.</li>
          <li class="benefit">Lets you use snail mail, email, texting, and social media to quickly market to your customers at very low cost.</li>
          <li class="benefit benefit--highlight">Web based which allows you to launch<br>media campaigns from your desktop,<br>or smartphone in moments.</li>
          <li class="benefit">Quick 3 - 5 minute training videos which give you hard hitting, quick action tips that will help you make your business better today.</li>
          <li class="benefit benefit--highlight">Live coaching calls to help motivate you to improve your business.</li>
          <li class="benefit">No contracts, or start up fees.<br>One low price of $299 per month.</li>
        </ul>
      </section>
      <section class="headline-band">
        <h1 class="headline">
          <span class="line-lead">Give us 5 minutes a day</span>
          <span class="line-bridge">and we will help you build</span>
          <span class="line-name">A Saffron</span>
          <span class="line-name-end">Ledger Works</span>
        </h1>
      </section>
      <div class="cash-image" role="img" aria-label="Photograph of a large pile of loose dollar bills on a dark surface"></div>
    </div>
  </main>
</body>
</html>
```